Landing page for offer process with similar products slider

We want to change our offer process. Customers will receive a link by email to a landing page, which shows the offer we created for them.
We quickly build a landing page with all the elements, which should also be in the final version, but the design is just random and only to show the idea. Please design us a landing page which looks much more attractive and state of the art.
Please note that under the offered items, there should be a slider with similar products. We are sending you the demo landing page. The colors should match our main web shop: kaminwelt-versand.example
Target Market(s)
Customers from 45yr. of age; homeowner
Industry/Entity Type
Stoves, fireplaces and chimney
Number of Pages Required
1 page
Look and feel
Each slider illustrates characteristics of the customer's brand and the style your logo design should communicate.

```html
<!DOCTYPE html>
<html lang="de">
<head>
<meta charset="utf-8">
<title>Ihr Angebot – Kaminwelt Versand</title>
<link href="https://fonts.googleapis.com/css2?family=Signika:wght@400;600;700&family=Open+Sans:wght@400;600&display=swap" rel="stylesheet">
<style>
:root{
  --orange:#f8b133;
  --orange-dark:#e99a12;
  --ink:#1f1f1f;
  --text:#333;
  --muted:#777;
  --panel:#efeeee;
  --band:#e3e2e2;
  --table-head:#555455;
  --cream:#fdf5e6;
  --footer:#3a3a3a;
  --white:#fff;
}
*{box-sizing:border-box;margin:0;padding:0}
html,body{width:1200px;height:3672px;overflow:hidden}
body{position:relative;background:var(--white);font-family:"Open Sans",sans-serif;color:var(--text);font-size:12px}
section,header,footer,nav,.abs{position:absolute}

/* top bar */
.topbar{top:0;left:0;width:1200px;height:26px;background:#ececec;font-size:8px;letter-spacing:.8px;color:#555}
.topbar .links{position:absolute;left:155px;top:8px;display:flex;gap:12px}
.topbar .links span{padding-right:12px;border-right:1px solid #999}
.topbar .links span:last-child{border:none}
.topbar .acct{position:absolute;right:146px;top:4px;display:flex;gap:8px}
.topbar .acct span{background:#ddd;padding:4px 8px;font-size:8px;letter-spacing:0}

.site-header{top:26px;left:0;width:1200px;height:64px;border-bottom:1px solid #e5e5e5}
.brand{position:absolute;left:150px;top:14px;display:flex;align-items:center;gap:8px}
.brand .dot{width:30px;height:30px;border-radius:50%;background:var(--orange)}
.brand b{font-family:"Signika",sans-serif;font-weight:600;font-size:17px;line-height:18px;color:#333}
.search{position:absolute;left:451px;top:16px;width:291px;height:32px;border:1px solid #ccc;border-radius:8px;overflow:hidden}
.search span{position:absolute;left:38px;top:8px;font-size:11px;color:#999}
.search i{position:absolute;right:0;top:0;width:36px;height:32px;background:var(--orange)}
.phone{position:absolute;right:146px;top:12px;text-align:right}
.phone b{font-family:"Signika",sans-serif;color:var(--orange);font-size:17px;font-weight:600}
.phone small{display:block;font-size:9px;color:#666}

.nav{top:90px;left:0;width:1200px;height:37px;border-bottom:1px solid #e5e5e5}
.nav .items{position:absolute;left:163px;top:9px;display:flex;gap:36px;font-family:"Signika",sans-serif;font-size:13px;color:#333}
.nav .items .stock{color:var(--orange)}
.nav .badges{position:absolute;right:146px;top:5px;display:flex;gap:6px}
.nav .badges i{width:26px;height:26px;border-radius:50%;border:3px solid #2d6fb5;background:#eef3fa}

/* offer details */
.offer{top:200px;left:71px;width:637px;height:746px;background:var(--panel);padding-top:24px;font-size:11px}
.offer .title{padding-left:56px;height:38px;font-family:"Signika",sans-serif;font-weight:600;font-size:12px;color:var(--ink)}
.offer .band{height:30px;line-height:30px;background:var(--band);padding-left:56px;font-family:"Signika",sans-serif;font-weight:600;font-size:12px;color:var(--ink)}
.offer .lines{padding:16px 0 12px 56px}
.offer .lines p{height:33px}

.paybox{top:200px;left:734px;width:416px;height:507px;background:var(--orange);text-align:center;color:var(--ink)}
.paybox .total{position:absolute;left:36px;top:42px;width:344px;height:40px;border:1.5px solid var(--ink);border-radius:8px;line-height:38px;font-family:"Signika",sans-serif;font-weight:600;font-size:14px}
.paybox .total b{font-size:16px}
.paybox .vat{position:absolute;top:97px;width:100%;font-size:11px}
.paybox .save{position:absolute;top:130px;width:100%;font-size:14px;line-height:27px}
.paybox .save b{font-family:"Signika",sans-serif;font-size:16px}
.paybox .btns{position:absolute;top:199px;left:60px;display:flex;gap:14px}
.paybox .btns span{width:141px;height:37px;line-height:37px;border-radius:6px;font-family:"Signika",sans-serif;font-weight:600;font-size:13px}
.btn-dark{background:#1e1e1e;color:var(--orange)}
.btn-light{background:var(--white);color:var(--ink)}
.paybox .date{position:absolute;top:258px;width:100%;font-family:"Signika",sans-serif;font-weight:600;font-size:12px}
.paymarks{position:absolute;top:298px;width:100%;display:flex;justify-content:center;gap:13px;font-family:"Signika",sans-serif;font-weight:600;font-size:11px;color:#2b2b2b}
.docs{position:absolute;top:330px;left:34px;width:348px}
.docs a{display:flex;align-items:center;justify-content:center;gap:10px;height:51px;border-bottom:1px solid #b97f14;font-size:11px;color:var(--ink);text-decoration:none}
.docs a:last-child{border:none}

/* table */
.items-table{top:1032px;left:74px;width:1076px;font-family:"Signika",sans-serif;font-size:12px}
table{width:1076px;border-collapse:collapse}
thead th{height:58px;background:var(--table-head);color:#fff;font-weight:600;border-left:2px solid #fff;text-align:center}
thead th:first-child{border-left:none}
thead th.name{text-align:left;padding-left:30px}
tbody td{background:var(--band);height:57px;text-align:center;font-weight:600;color:var(--ink)}
tbody td.name{text-align:left;padding-left:30px}
tbody tr.first td{border-bottom:1px solid #b9b9b9}
.net{height:47px;background:var(--table-head);color:#fff;font-weight:600;display:flex;justify-content:space-between;align-items:center;padding:0 34px 0 36px}
.sums{background:var(--band);height:90px;padding:18px 34px 0 36px;font-weight:600;color:var(--ink)}
.sums p{display:flex;justify-content:space-between;height:30px}

.notes{top:1413px;left:0;width:1200px;font-family:"Signika",sans-serif;font-weight:600;font-size:12px;color:#333}
.notes .row{display:flex;justify-content:center;gap:34px;height:49px}
.notes span{display:flex;align-items:center;gap:10px;height:26px}

/* guarantee band */
.guarantee{top:1566px;left:0;width:1200px;height:383px}
.guarantee .bg{position:absolute;inset:0;background:linear-gradient(180deg,#f6b23a,#f2a928 60%,#f6b33c)}
.stamp{position:absolute;left:412px;top:50px;width:376px;height:56px;border:4px solid #222;border-radius:4px;text-align:center;line-height:48px;font-family:"Signika",sans-serif;font-weight:700;font-size:32px;letter-spacing:2px;color:#222}
.perks{position:absolute;left:130px;top:148px;width:940px;font-family:"Signika",sans-serif;font-weight:600;font-size:15px;color:#1e1e1e}
.perks .row{display:flex;justify-content:space-between;height:58px}
.perks span{display:flex;align-items:center;gap:10px}
.seals{position:absolute;top:270px;left:390px;display:flex;align-items:center;gap:40px}
.seals i{width:70px;height:70px;border-radius:50%;background:#fff;border:5px solid #2f74b8}
.seals .partner{display:flex;align-items:center;gap:14px;font-family:"Signika",sans-serif;font-weight:700;font-size:24px;color:#1e2f6b}
.seals .partner small{font-size:14px;font-weight:600;border-left:2px solid #1e2f6b;padding-left:14px;line-height:16px}

/* sliders */
.slider{left:0;width:1200px;text-align:center}
.slider h2{font-family:"Signika",sans-serif;font-weight:600;font-size:22px;color:var(--ink);letter-spacing:.5px}
.slider .lead{width:880px;margin:18px auto 0;font-size:12.5px;line-height:24px;color:#333}
.cards{position:absolute;left:141px;display:flex;gap:20px}
.card{width:292px;height:292px;background:var(--white);box-shadow:0 2px 10px rgba(0,0,0,.06);position:relative}
.card .ph{position:absolute;left:36px;top:36px;width:220px;height:220px;border-radius:6px}
.arrow{position:absolute;width:60px;height:60px;border-radius:50%;display:flex;align-items:center;justify-content:center}
.arrow.prev{left:51px;background:#fff;box-shadow:0 2px 10px rgba(0,0,0,.08)}
.arrow.next{left:1086px;background:var(--orange)}
.related{top:2020px;height:520px}
.standard{top:2594px;height:574px;background:var(--cream);padding-top:46px}
.card .prod-title{position:absolute;top:166px;width:100%;font-family:"Signika",sans-serif;font-weight:600;font-size:14px;color:var(--ink);letter-spacing:.5px}
.card .prod-desc{position:absolute;top:192px;width:100%;font-size:12px}
.card .add{position:absolute;top:220px;left:95px;width:102px;height:37px;line-height:37px;border-radius:7px;background:var(--orange);font-family:"Signika",sans-serif;font-weight:600;font-size:13px;color:var(--ink)}

/* footer */
.site-footer{top:3168px;left:0;width:1200px;height:504px;background:var(--footer);color:#fff}
.site-footer h3{position:absolute;top:78px;font-family:"Signika",sans-serif;font-weight:400;font-size:17px}
.fmarks{position:absolute;display:flex;gap:16px;align-items:center;font-family:"Signika",sans-serif;font-weight:600;font-size:14px}
.fmarks .c{width:20px;height:20px;border-radius:50%;background:#fff;display:inline-block;margin-right:4px;vertical-align:middle}
.site-footer .rule{position:absolute;left:135px;width:930px;height:1px;background:#8a8a8a}
.qtitle{position:absolute;left:145px;top:260px;font-size:10px;font-weight:600;text-decoration:underline}
.qcol{position:absolute;top:286px;font-size:10px;line-height:18.5px}
.support{position:absolute;left:296px;top:395px;font-family:"Signika",sans-serif;font-weight:600;font-size:15px;color:var(--orange)}
.consult{position:absolute;right:145px;top:260px;text-align:right;font-size:10px;line-height:18.5px}
.consult b{font-weight:600}
.social{position:absolute;right:145px;top:456px;display:flex;gap:6px}
.social span{width:27px;height:27px;border-radius:50%;background:#fff;color:var(--footer);font-size:6px;font-weight:600;display:flex;align-items:center;justify-content:center}
</style>
</head>
<body>

<div class="abs topbar">
  <div class="links"><span>SICHER EINKAUFEN ▾</span><span>VORTEILE ▾</span><span>BERATUNG &amp; KONTAKT ▾</span></div>
  <div class="acct"><span>Mein Konto</span><span>Warenkorb</span></div>
</div>

<header class="site-header">
  <div class="brand"><span class="dot"></span><b>KAMINWELT<br>VERSAND</b></div>
  <div class="search"><span>Suchbegriff oder Artikelnummer</span><i></i></div>
  <div class="phone">
    <b><svg width="14" height="14" viewBox="0 0 24 24" fill="#f8b133"><path d="M6.6 10.8a15.1 15.1 0 0 0 6.6 6.6l2.2-2.2c.3-.3.7-.4 1-.2 1.1.4 2.3.6 3.6.6.6 0 1 .4 1 1V20c0 .6-.4 1-1 1A17 17 0 0 1 3 4c0-.6.4-1 1-1h3.5c.6 0 1 .4 1 1 0 1.3.2 2.5.6 3.6.1.3 0 .7-.2 1z"/></svg> 0800 412 733 0</b>
    <small>Mo. - Fr. von 09:00 bis 18:00 Uhr</small>
  </div>
</header>

<nav class="nav">
  <div class="items"><span>Online-Shop ⌄</span><span>Service ⌄</span><span class="stock">| Lagernd - sofort verfügbar!</span></div>
  <div class="badges"><i></i><i></i><i></i></div>
</nav>

<section class="offer">
  <div class="title">Angebot Nr. 128471</div>
  <div class="band">Käufer:</div>
  <div class="lines"><p>Marko Lindner</p><p>Lindenweg 12</p><p>04109 Leipzig</p><p>GERMANY</p></div>
  <div class="band">Lieferadresse des Käufer:</div>
  <div class="lines"><p>Marko Lindner</p><p>Lindenweg 12</p><p>10115 Berlin</p><p>GERMANY</p></div>
  <div class="band">Rechnungs-Details:</div>
  <div class="lines"><p>Rearbeter : Teet nicknamel</p><p>Kunden-ir : 235024</p><p>Datum : 2024-05-22 10:1439</p></div>
  <div class="band">Verkäufer</div>
  <div class="lines"><p>Ofenhaus GmbH|</p><p>Beispielstr. 18</p><p>80331 München</p></div>
</section>

<section class="paybox">
  <div class="total">Sie zahlen: <b>3.431,09 €</b></div>
  <p class="vat">inkl. MwSt und Vers</p>
  <p class="save"><b>Sie sparen 98,94 €</b> gegenüber dem<br>Einzelkauf |</p>
  <div class="btns"><span class="btn-dark">Submit</span><span class="btn-light">Send PDF</span></div>
  <p class="date">Voraussichtliches Lieferdatum</p>
  <div class="paymarks"><span>Paylo</span><span>QuickPay</span><span>Ratenfix</span><span>Kartex</span><span>Bankdirekt</span><span>NetPay</span></div>
  <div class="docs">
    <a href="#"><svg width="16" height="20" viewBox="0 0 16 20"><path d="M1 1h9l5 5v13H1z" fill="none" stroke="#222" stroke-width="1.4"/><path d="M10 1v5h5" fill="none" stroke="#222" stroke-width="1.4"/></svg>Benutzerhandbuch Kaminofen Nordlicht</a>
    <a href="#"><svg width="16" height="20" viewBox="0 0 16 20"><path d="M1 1h9l5 5v13H1z" fill="none" stroke="#222" stroke-width="1.4"/><path d="M10 1v5h5" fill="none" stroke="#222" stroke-width="1.4"/></svg>Produkt Datenblatt Kaminofen Nordlicht</a>
    <a href="#"><svg width="16" height="20" viewBox="0 0 16 20"><path d="M1 1h9l5 5v13H1z" fill="none" stroke="#222" stroke-width="1.4"/><path d="M10 1v5h5" fill="none" stroke="#222" stroke-width="1.4"/></svg>Benutzerhandnuch Kaminofen Nordlicht Plus 2.0</a>
  </div>
</section>

<section class="items-table">
  <table>
    <colgroup><col style="width:96px"><col style="width:409px"><col style="width:60px"><col style="width:125px"><col style="width:70px"><col style="width:70px"><col style="width:117px"><col style="width:129px"></colgroup>
    <thead><tr><th>Pos.</th><th class="name">Bezelchnung</th><th>ID</th><th>Delivery time</th><th>Anz.</th><th>Ust.</th><th>Brutto Prels</th><th>Brutto Gesamt</th></tr></thead>
    <tbody>
      <tr class="first"><td>1</td><td class="name">Kaminofen Nordlicht 6 kW</td><td>9</td><td>DT</td><td>1</td><td>19%</td><td>318.99€</td><td>318.99€</td></tr>
      <tr><td>1</td><td class="name">Kaminofen Fjord W+ 2.0 | 7 kW Speicherofen |</td><td>9</td><td>DT</td><td>1</td><td>19%</td><td>3.112,10€</td><td>3.112,10€</td></tr>
    </tbody>
  </table>
  <div style="height:18px;background:var(--band)"></div>
  <div class="net"><span>Gesamtkosten Netto:</span><span>2.779.18 €</span></div>
  <div class="sums"><p><span>zzgl. 19% USt</span><span>547.82€</span></p><p><span>Gesamtkosten:</span><span>3.431.09€</span></p></div>
</section>

<section class="notes">
  <div class="row">
    <span><svg width="18" height="18" viewBox="0 0 18 18"><path d="M3 2l12 7-12 7 4-7z" fill="none" stroke="#333" stroke-width="1.6"/></svg>Gewahre Versandart: Standardversand DE testl</span>
    <span><svg width="18" height="18" viewBox="0 0 18 18"><path d="M3 2l12 7-12 7 4-7z" fill="none" stroke="#333" stroke-width="1.6"/></svg>Angebot freibleibend. Änderung der Tagespreise möglich.</span>
  </div>
  <div class="row">
    <span><svg width="18" height="18" viewBox="0 0 18 18"><path d="M3 2l12 7-12 7 4-7z" fill="none" stroke="#333" stroke-width="1.6"/></svg>Vielen herzlichen Dank für Ihre Antrage bei kaminwelt-versand.example.</span>
  </div>
</section>

<section class="guarantee">
  <div class="bg" role="img" aria-label="Warm getönte Küchenszene mit Dunstabzug und Hängelampen als Hintergrund"></div>
  <div class="stamp">BESTPREISGARANTIE</div>
  <div class="perks">
    <div class="row">
      <span><svg width="20" height="20" viewBox="0 0 18 18"><path d="M3 2l12 7-12 7 4-7z" fill="none" stroke="#1e1e1e" stroke-width="1.6"/></svg>Markenhändler mit Zertifizierung</span>
      <span><svg width="20" height="20" viewBox="0 0 18 18"><path d="M3 2l12 7-12 7 4-7z" fill="none" stroke="#1e1e1e" stroke-width="1.6"/></svg>Größter Kamineinzelhändler Deutschlands</span>
      <span><svg width="20" height="20" viewBox="0 0 18 18"><path d="M3 2l12 7-12 7 4-7z" fill="none" stroke="#1e1e1e" stroke-width="1.6"/></svg>Kostenlose Fachberatung</span>
    </div>
    <div class="row">
      <span><svg width="20" height="20" viewBox="0 0 18 18"><path d="M3 2l12 7-12 7 4-7z" fill="none" stroke="#1e1e1e" stroke-width="1.6"/></svg>Garantierter Datenschutz</span>
      <span><svg width="20" height="20" viewBox="0 0 18 18"><path d="M3 2l12 7-12 7 4-7z" fill="none" stroke="#1e1e1e" stroke-width="1.6"/></svg>Vorkasse vollständig über Sicherpartner Trade abgesichert</span>
      <span><svg width="20" height="20" viewBox="0 0 18 18"><path d="M3 2l12 7-12 7 4-7z" fill="none" stroke="#1e1e1e" stroke-width="1.6"/></svg>Sichere Abwicklung und Lieferung</span>
    </div>
  </div>
  <div class="seals"><i></i><i></i><div class="partner">Sicherpartner<small>Trade</small></div></div>
</section>

<section class="slider related">
  <h2>Verwandte Produzenten</h2>
  <p class="lead">"Lorem ipsum dolor sit amet, consectetur adipiscing elit, sed do eiusmod tempor incididunt ut labore et dolore magna aliqua. Ut enim ad minim veniam, quis nostrud exercitation ullamco laboris nisi ut aliquip ex ea commodo consequat. Duis aute irure dolor in reprehenderit in voluptate velit esse cillum dolore eu fugiat nulla pariatur. Excepteur sint occaecat cupidatat non proident, sunt in culpa qui officia deserunt mollit anim id est laborum."</p>
  <div class="cards" style="top:193px">
    <div class="card"><div class="ph" role="img" aria-label="Produktfoto Schornsteinabdeckung aus Edelstahl" style="background:linear-gradient(135deg,#f4f4f4,#c9c9c9)"></div></div>
    <div class="card"><div class="ph" role="img" aria-label="Produktfoto Wanddurchführung mit Dämmplatten" style="background:linear-gradient(135deg,#f1efe8,#cfcac0)"></div></div>
    <div class="card"><div class="ph" role="img" aria-label="Produktfoto schwarzes Ofenrohr-Knie" style="background:linear-gradient(135deg,#f3f3f3,#3a3a3a)"></div></div>
  </div>
  <div class="arrow prev" style="top:309px"><svg width="16" height="24" viewBox="0 0 16 24"><path d="M13 2L3 12l10 10" fill="none" stroke="#f8b133" stroke-width="2.5"/></svg></div>
  <div class="arrow next" style="top:309px"><svg width="16" height="24" viewBox="0 0 16 24"><path d="M3 2l10 10L3 22" fill="none" stroke="#fff" stroke-width="2.5"/></svg></div>
</section>

<section class="slider standard">
  <h2>The Standard Lorem Lpsum Passage, Used Since The 1500s</h2>
  <p class="lead">"Lorem ipsum dolor sit amet, consectetur adipiscing elit, sed do eiusmod tempor incididunt ut labore et dolore magna aliqua. Ut enim ad minim veniam, quis nostrud exercitation ullamco laboris nisi ut aliquip ex ea commodo consequat. Duis aute irure dolor in reprehenderit in voluptate velit esse cillum dolore eu fugiat nulla pariatur. Excepteur sint occaecat cupidatat non proident, sunt in culpa qui officia deserunt mollit anim id est laborum."</p>
  <div class="cards" style="top:233px">
    <div class="card"><div class="ph" role="img" aria-label="Produktfoto Dachdurchführung mit Schornsteinrohr" style="background:linear-gradient(135deg,#f3efee,#9a5b4c)"></div></div>
    <div class="card"><div class="ph" role="img" aria-label="Produktfoto Edelstahl-Reinigungstür" style="background:linear-gradient(135deg,#f4f4f4,#a9a9a9)"></div></div>
    <div class="card">
      <div class="ph" role="img" aria-label="Produktfoto schwarzer Kaminofen mit Sichtfenster" style="left:116px;top:30px;width:60px;height:110px;background:linear-gradient(180deg,#2a2a2a,#555)"></div>
      <p class="prod-title">61-3622-1551 ORBIT FIXED</p>
      <p class="prod-desc">Additional description goes here</p>
      <span class="add">ADD</span>
    </div>
  </div>
  <div class="arrow prev" style="top:379px"><svg width="16" height="24" viewBox="0 0 16 24"><path d="M13 2L3 12l10 10" fill="none" stroke="#f8b133" stroke-width="2.5"/></svg></div>
  <div class="arrow next" style="top:379px"><svg width="16" height="24" viewBox="0 0 16 24"><path d="M3 2l10 10L3 22" fill="none" stroke="#fff" stroke-width="2.5"/></svg></div>
</section>

<footer class="site-footer">
  <h3 style="left:145px">Payment Methods</h3>
  <h3 style="right:145px">Shipping methods</h3>
  <div class="fmarks" style="left:145px;top:132px"><span><i class="c"></i>VORKASSE</span><span><i class="c"></i>Cardo</span><span>Paylo</span><span>QuickPay</span><span>Ratenfix</span><span>Kartex</span><span>Bankdirekt</span><span>NetPay</span></div>
  <div class="fmarks" style="left:145px;top:180px"><span>Epay</span><span>Kreditleicht</span></div>
  <div class="fmarks" style="right:145px;top:132px"><span>Fraktline</span><span>Paketo</span><span>Logista</span></div>
  <div class="rule" style="top:222px"></div>
  <p class="qtitle">Quick links</p>
  <div class="qcol" style="left:145px">glossary<br>About Us<br>revocation<br>data protection<br>imprint<br>Blog</div>
  <div class="qcol" style="left:296px">Frequently asked questions<br>Conditions<br>delivery<br>Ordering process<br>Contact us</div>
  <p class="support">Support</p>
  <div class="consult"><b>Free consultation</b><br><br>0800 412 733 0<br>Mon. - Fri. from 09:00 to 18:00<br>info@kaminwelt-versand.example</div>
  <div class="rule" style="top:439px"></div>
  <div class="social"><span>Kanal</span><span>Forum</span><span>News</span><span>Pins</span></div>
</footer>

</body>
</html>
```